I work in creative/artistic projects across different mediums.
It needs to communicate creativity, style, sexy, uniqueness, individuality and sophistication.
It should not look corporate.
Colours I like are black silver gold deep purple, chocolate, orchid.
It doesn't have to make use of all these colours.
I do not like bright primary colors.
Updates

Project Deadline Extended
Reason: Still in the communication process and to allow the person enough time to finish the design. Though i should know in the next day or two. Thank you.

Target Market(s)

creatives and companies wanting to inject creativity into thier business.

Industry/Entity Type

Work

Contact Information for Business Card

Lionel Crowthwick
0418359026
lionel@lionelcrowthwick.com

quietsilverhour.com.au

Requirements
Should not have
• Anything corporate OR OLD FASHIONED

```html
<!DOCTYPE html>
<html lang="en">
<head>
<meta charset="utf-8">
<title>Lionel Crowthwick – Business Card</title>
<link href="https://fonts.googleapis.com/css2?family=Mulish:wght@600;700;800&display=swap" rel="stylesheet">
<style>
  :root {
    --stage: #f2f4f5;
    --card-black: #231f20;
    --chocolate: #7f5230;
    --mocha: #a87a51;
    --caramel: #c29a6b;
    --seam: #2e241e;
    --swirl-brown: #9a6a44;
    --swirl-grey: #4d4b4c;
    --ink-light: #ffffff;
    --name-gold: #c09a6c;
  }
  html, body {
    margin: 0;
    padding: 0;
    width: 1200px;
    height: 761px;
    overflow: hidden;
    background: var(--stage);
  }
  .business-card {
    position: absolute;
    left: 283px;
    top: 175px;
    width: 630px;
    height: 388px;
    display: block;
  }
  .card-base { fill: var(--card-black); }
  .band-outer { fill: var(--caramel); }
  .band-middle { fill: var(--mocha); }
  .band-inner { fill: var(--chocolate); }
  .band-seam { fill: none; stroke: var(--seam); stroke-width: 3; }
  .contact-line {
    font-family: "Mulish", "Century Gothic", sans-serif;
    font-weight: 700;
    font-size: 20px;
    fill: var(--ink-light);
    letter-spacing: 0.2px;
  }
  .contact-icon { fill: var(--ink-light); }
  .contact-icon-stroke { fill: none; stroke: var(--ink-light); stroke-width: 2; }
  .holder-name {
    font-family: "Mulish", "Century Gothic", sans-serif;
    font-weight: 800;
    font-size: 38px;
    fill: var(--name-gold);
  }
</style>
</head>
<body>
<svg class="business-card" viewBox="0 0 630 388" xmlns="http://www.w3.org/2000/svg" aria-label="Business card for Lionel Crowthwick">
  <defs>
    <radialGradient id="brown-flourish-tone" cx="0.5" cy="0.5" r="0.5">
      <stop offset="0" stop-color="var(--swirl-brown)" stop-opacity="0.7"/>
      <stop offset="1" stop-color="var(--swirl-brown)" stop-opacity="0"/>
    </radialGradient>
    <radialGradient id="grey-flourish-tone" cx="0.5" cy="0.5" r="0.5">
      <stop offset="0" stop-color="var(--swirl-grey)" stop-opacity="0.55"/>
      <stop offset="1" stop-color="var(--swirl-grey)" stop-opacity="0"/>
    </radialGradient>
    <clipPath id="card-edge"><rect width="630" height="388"/></clipPath>
    <path id="arc-phone" d="M0 212 A258 212 0 0 0 258 0"/>
    <path id="arc-email" d="M0 276 A322 276 0 0 0 322 0"/>
    <path id="arc-web" d="M0 356 A404 356 0 0 0 404 0"/>
  </defs>

  <g clip-path="url(#card-edge)">
    <rect class="card-base" width="630" height="388"/>

    <rect x="250" y="20" width="380" height="368" fill="url(#grey-flourish-tone)"
          role="img" aria-label="Faint grey scrolling flourishes across the black field"/>

    <ellipse class="band-outer" cx="0" cy="0" rx="420" ry="372"/>
    <ellipse class="band-seam" cx="0" cy="0" rx="421" ry="373"/>
    <ellipse class="band-middle" cx="0" cy="0" rx="334" ry="288"/>
    <ellipse class="band-seam" cx="0" cy="0" rx="335" ry="289"/>
    <ellipse class="band-inner" cx="0" cy="0" rx="267" ry="220"/>
    <ellipse class="band-seam" cx="0" cy="0" rx="268" ry="221"/>

    <ellipse cx="120" cy="80" rx="110" ry="80" fill="url(#brown-flourish-tone)"
             role="img" aria-label="Soft tan swirl flourish on the chocolate band"/>
  </g>

  <!-- phone -->
  <g class="contact-icon" transform="translate(52 158)">
    <path d="M6 2 L12 0 L17 10 L13 13 C15 19 19 24 25 27 L28 23 L38 29 L36 35 C28 38 12 30 5 16 C3 10 3 5 6 2 Z"/>
  </g>
  <text class="contact-line"><textPath href="#arc-phone" startOffset="30%">0418 359 026</textPath></text>

  <!-- email -->
  <g transform="translate(52 236)">
    <rect class="contact-icon" x="0" y="0" width="36" height="24"/>
    <path d="M0 0 L18 14 L36 0 M0 24 L14 11 M36 24 L22 11" fill="none" stroke="var(--mocha)" stroke-width="2"/>
  </g>
  <text class="contact-line"><textPath href="#arc-email" startOffset="20%">lionel@lionelcrowthwick.com</textPath></text>

  <!-- web -->
  <g transform="translate(72 327)">
    <circle class="contact-icon-stroke" r="17" stroke-width="3"/>
    <ellipse class="contact-icon-stroke" rx="7" ry="17"/>
    <line class="contact-icon-stroke" x1="-17" y1="0" x2="17" y2="0"/>
    <line class="contact-icon-stroke" x1="-14" y1="-9" x2="14" y2="-9"/>
    <line class="contact-icon-stroke" x1="-14" y1="9" x2="14" y2="9"/>
  </g>
  <text class="contact-line"><textPath href="#arc-web" startOffset="19%">www.quietsilverhour.com.au</textPath></text>

  <text class="holder-name" x="591" y="337" text-anchor="end">Lionel Crowthwick</text>
</svg>
</body>
</html>
```